Blood Testing Health App

We are looking for a graphics designer to create a web app for us so that we may insert it into a health management website system.
For branding purposes we are at www.Veritamed.com and we are revamping our website... Example of new colors attached.
How we work...
We are a blood testing company based in the USA.
We offer a blood testing service nationwide in the USA.
We allow customers to order tests directly from us, visit a lab, have their blood drawn, or submit a urine sample, the lab tests it and they send the results back to our computer system and we share it with the customer.
The benefits of this are the customer does not need to go to the doctor and pay for the doctors visit to order these tests, which save them money. The tests are cheaper than going through the doctor. The customer simply uses us to get the test and the results and they can then take the results to their doctor... this process has saved them money. Others may be interested in regular check ups for blood work etc... and this allows them to do it with out needing a doctor, or if you have no insurance, this is a cheaper option too. We are quicker than a doctor, customers do not need appointments etc.
Hopefully you now have a better understanding as to what we do.
Here is the spec.
The app screen size is 750 px wide by 700 px high. ( A pdf is attached to show where the app is going to go, it is on page 3 of the pdf) The customer will have the ability to scroll… therefore the length of the page can be longer.
The app will consist of the following sections
Entry Page –
This will be the first page the user sees upon opening the app. This will be where they are directed from to the sections of the app discussed below. This needs to be branded for VeritaMed with a modern look.
1 – Order Test (Giving them the ability to purchase a blood test within the app)
2 – VeritaMed Dashboard (A dashboard that has everything they could need to use our service_
How it works Section on entry page – this will be a simple set of graphics showing how the service works. We already have the graphics for this, they do not need to be built again. They are attached to this brief
Basic structure of sections –
Order Test –
This page contains all tests, filed in categories – and Sub categories – Each test needs a link to an Information section – Price – Buy Now – Cart Process
VeritaMed Dashboard –
A page of icons along the top of the app
- My Confirmation
- My Nearest Lab
- My Receipt
- My Orders
- My Account
- My Results
- My Inbox
- Contact Us
Sections in more detail -
Order A Test –
Show all categories/ sub categories – There are 23 categories, 14 sub categories, and within these categories are 300 tests - Here is the information for the categories etc - http://www.veritamed.com/panels.aspx?PanelGroupID=4 Just in case it helps :)
We need to present this in a graphic format that is spacious, modern (quillbox, taskhub web appearance is the direction we are going for) We need it to be clear and not overwhelming to the customer.
Functionality idea…
Customer clicks category/ subcategory and tests appear.
Customer sees small 35 word description. For more information the test opens into a lightbox or expand the container which ever graphic designer believes to be most visually appealing
Buy Now must always be visible, along with price of the test
Buying process explained – Customer clicks buy now –
They are then taken to a Review Order screen ( This contains Order summary and choose payment method – insert payment details )
– Confirm payment –
Confirmation screen appears, thanking them.
They are then taken to the VeritaMed Dashboard...
VeritaMed Dashboard –
"My Confirmation" - Print Confirmation Order (PDF is in brief, we want this web based not a pdf download)
"My Nearest Lab Location" - This does not need to be designed because the web developer has this part under control, but we do need the icon in the dashboard
"My Receipt" - Print receipt - This does not exist in our system yet. So we need to create this from scratch - It will need to have - The test they are purchasing and the amount of the test - The customers name - The order ID - Must provide printer friendly option too
"My Orders" - This will have a list of orders - At the end of each order will be a status update of either "Test results" "Open order"
A graphic table format would be perfect. This will be linked to relevant results if they have been received. I have also attached a version of what the customer currently sees on our website. We know it is nasty ;) We are redesigning... but the information is there for this section to help design it with the right info. If the results are ready it will say in this list.
"Results Ready" will be a link to show those results once the customer has clicked the link, and the results will appear in the app, under the icons. There must be a printer friendly version too.
"My Results" Developer will sort this page out but we need the icon... It will be exactly like my orders but only show test results
"My Account" - This will be a place for them to update their personal information - Name, DOB, Address, Email Address
"My Inbox" - An inbox interface - Our way of contacting the customer for promotions we are running etc – We need a design of how this screen will appear. We also need the icon in the dashboard to have a notification on it if there are messages in the customers inbox. A little red 1, or circle with number of messages in the inbox.
"Customer Service" - This does not need to be designed because the web developer has this part under control, but we do need the icon in the dashboard
Icons appear along the top of app ( example - Mac icons/ iphone app icons) When the customer clicks an icon the content always appears below the icons
Here is more information for the icons and what should appear when each icon is clicked.
Screens to be designed –
Entry Page
Order A Test Page
Review Order Screen/Payment Screen - Show a lightbox that shows payment has been confirmed. Customer clicks close and are on the Confirmation Screen
VeritaMed Dashboard - Screens mentioned in detail above
We can't wait to see your designs!
Please email any questions.
Hi all this is the first time we have used pixel forum and understand the budget was too low for this project. We have now increased the budget to $2,000 and extended the deadline by another week
Hi all we are receiving some really great designs. I just added an example of the space that the web app will be going into... It is called "kelvraapp.pdf"
Hi guys updated the brief. Hopefully this will help with the dashboard part of the design

```html
<!DOCTYPE html>
<html lang="en">
<head>
<meta charset="utf-8">
<title>VeritaMed – Shopping Cart</title>
<link rel="stylesheet" href="https://fonts.googleapis.com/css2?family=Open+Sans:wght@400;600&display=swap">
<style>
  :root {
    --brand-dark: #5a1e1e;
    --olive: #8a9b34;
    --olive-light: #a7b856;
    --lime: #8cb414;
    --lime-deep: #79a114;
    --row-bg: #ebebeb;
    --row-line: #ffffff;
    --text: #2b2b2b;
    --muted: #8a8a8a;
    --white: #ffffff;
  }
  * { box-sizing: border-box; margin: 0; padding: 0; }
  html, body { width: 692px; height: 1200px; overflow: hidden; background: var(--white); }
  body { font-family: "Open Sans", Arial, sans-serif; color: var(--text); position: relative; }

  .brand-header { height: 138px; display: flex; align-items: center; justify-content: center; gap: 14px; }
  .brand-mark { width: 30px; height: 30px; background: var(--lime); }
  .brand-name { font-size: 50px; font-weight: 600; color: var(--brand-dark); letter-spacing: -1px; }

  .page-title {
    height: 77px;
    background: linear-gradient(90deg, var(--olive) 0%, var(--olive-light) 100%);
    color: var(--white); font-size: 36px; text-align: center; line-height: 77px;
  }
  .payment-note {
    height: 196px; background: var(--lime); color: var(--white);
    font-size: 21.5px; line-height: 32px; text-align: center;
    padding: 34px 60px 0;
  }

  .cart-table { position: absolute; left: 35px; top: 503px; width: 622px; border-collapse: collapse; }
  .cart-table th {
    background: var(--lime-deep); color: var(--white); font-weight: 400; font-size: 26px;
    height: 62px; text-align: left;
  }
  .cart-table td { background: var(--row-bg); height: 81px; font-size: 25px; border-top: 2px solid var(--row-line); }
  .col-name { padding-left: 30px; width: 412px; }
  .col-price { width: 125px; }
  .col-action { text-align: center; border-left: 2px solid #c8c8c8; }
  .cart-table td.col-action { border-left: 2px solid #c8c8c8; }
  .cart-icon { display: block; margin: 0 auto; }

  .coupon-input {
    position: absolute; left: 72px; top: 840px; width: 553px; height: 60px;
    border: 1.5px solid #9a9a9a; background: var(--white);
  }
  .coupon-button {
    position: absolute; left: 152px; top: 923px; width: 406px; height: 65px;
    background: linear-gradient(180deg, #85ad1c 0%, #6a9412 100%);
    color: var(--white); font-size: 35px; text-align: center; line-height: 65px;
  }

  .cart-links {
    position: absolute; left: 0; top: 1112px; width: 692px; text-align: center;
    font-size: 21px; color: var(--lime-deep);
  }
  .cart-links .sep { margin: 0 12px; color: var(--lime-deep); }

  .footer-stripe { position: absolute; left: 0; bottom: 0; width: 692px; height: 28px; display: flex; }
  .footer-stripe span { flex: 1; }
</style>
</head>
<body>
  <header class="brand-header">
    <span class="brand-mark"></span>
    <span class="brand-name">VeritaMed</span>
  </header>

  <h1 class="page-title">Contents of Your Shopping Cart</h1>
  <p class="payment-note">This site uses financial encryption for secure payment processing. By clicking the "Secure Checkout" button below you may pay for your order with a credit card or through your PayWallet account.</p>

  <table class="cart-table">
    <thead>
      <tr><th class="col-name">Item Name</th><th class="col-price">Price</th><th class="col-action"></th></tr>
    </thead>
    <tbody>
      <tr><td class="col-name">Amenorrhea Profile</td><td class="col-price">$105.00</td><td class="col-action">
        <svg class="cart-icon" width="46" height="46" viewBox="0 0 46 46"><circle cx="23" cy="23" r="21" fill="#f7f7f7" stroke="#555" stroke-width="2"/><path d="M11 15h4l4 13h14l3-9H17" fill="none" stroke="#444" stroke-width="2"/><circle cx="20" cy="32" r="2" fill="#444"/><circle cx="31" cy="32" r="2" fill="#444"/></svg>
      </td></tr>
      <tr><td class="col-name">CA-125</td><td class="col-price">$65.00</td><td class="col-action">
        <svg class="cart-icon" width="46" height="46" viewBox="0 0 46 46"><circle cx="23" cy="23" r="21" fill="#f7f7f7" stroke="#555" stroke-width="2"/><path d="M11 15h4l4 13h14l3-9H17" fill="none" stroke="#444" stroke-width="2"/><circle cx="20" cy="32" r="2" fill="#444"/><circle cx="31" cy="32" r="2" fill="#444"/></svg>
      </td></tr>
      <tr><td class="col-name">Calcium, Ionized, Serum</td><td class="col-price">$126.00</td><td class="col-action">
        <svg class="cart-icon" width="46" height="46" viewBox="0 0 46 46"><circle cx="23" cy="23" r="21" fill="#f7f7f7" stroke="#555" stroke-width="2"/><path d="M11 15h4l4 13h14l3-9H17" fill="none" stroke="#444" stroke-width="2"/><circle cx="20" cy="32" r="2" fill="#444"/><circle cx="31" cy="32" r="2" fill="#444"/></svg>
      </td></tr>
    </tbody>
  </table>

  <div class="coupon-input"></div>
  <div class="coupon-button">Apply Coupon Code</div>

  <nav class="cart-links">
    Secure Checkout<span class="sep">|</span>Empty Shopping Cart<span class="sep">|</span>Continue Shopping
  </nav>

  <div class="footer-stripe">
    <span style="background:#7d9e1a"></span>
    <span style="background:#94b82a"></span>
    <span style="background:#a9c640"></span>
    <span style="background:#86a91e"></span>
    <span style="background:#b5cf55"></span>
    <span style="background:#9bbd2e"></span>
  </div>
</body>
</html>
```